Real Estate Brokerage Informational Handbill

A 4 X 6 handbill to promote a real estate brokerage modeled after the design attached including attached logo and information.
These handbills should provide a high-level overview of what we do at the brokerage and should be attractive and be inviting.
The goal of the handbill is to have motivated clients in the market to buy or sell their home or property call or visit our website

Target Market(s)

Buyers and sellers of real estate in the Rochester NY area ages 24 - 60

Industry/Entity Type

Real Estate

Font styles to use
Sans Serif

Requirements
Must have
• Please include all the information contained on current handbill
• remove the line "we will walk you through the home buying process at no cost to you".
• replace with "come to one of our monthly first-time buyer informational sessions".
• add the phrase "have your reviewed and receive customized Home Purchase Plan"
• Add the slogan "Bright Path Realty Helping Motivated People Achieve Their Real Estate Goals"
Nice to have
• 2 sided design

```html
<!DOCTYPE html>
<html lang="en">
<head>
<meta charset="utf-8">
<title>Bright Path Realty Handbill</title>
<link href="https://fonts.googleapis.com/css2?family=Noto+Serif:wght@400;700&display=swap" rel="stylesheet">
<style>
:root{
  --page:#ffffff;
  --slate:#31343d;
  --slate-deep:#2a2d35;
  --ink:#1f2a3a;
  --white:#ffffff;
  --silver:#d2d3d6;
  --sky-top:#c9d6e2;
  --sky-mid:#eef3f7;
  --skin:#d9b49c;
  --rule:#c8a58a;
}
*{margin:0;padding:0;box-sizing:border-box}
html,body{width:1200px;height:900px;overflow:hidden;background:var(--page)}
body{position:relative;font-family:"Noto Serif",Georgia,serif;color:var(--white)}
.card{position:absolute;top:18px;height:864px;overflow:hidden}
.card--front{left:17px;width:576px;background:var(--sky-mid)}
.card--back{left:608px;width:575px;background:var(--slate)}
.photo{position:absolute;inset:0}
.photo--key{background:linear-gradient(160deg,var(--sky-top) 0%,var(--sky-mid) 45%,#f7f9fb 70%,var(--skin) 100%)}
.photo--faint{background:radial-gradient(ellipse at 30% 40%,#3a3e48 0%,var(--slate) 55%,var(--slate-deep) 100%)}
.swoosh{position:absolute;left:0;top:0;width:576px;height:864px}
.centered{position:absolute;text-align:center}
.brand{font-weight:700;font-size:28px;line-height:36px}
.brand--front{left:253px;width:330px;top:128px;color:var(--ink)}
.brand--back{left:0;width:575px;top:128px}
.slogan{left:253px;width:330px;top:240px;font-weight:700;font-size:18px;line-height:24px;color:var(--ink)}
.intro{left:243px;width:330px;top:314px;font-size:14px;line-height:19.3px;color:var(--ink)}
.invite{left:0;width:576px;top:742px;font-weight:700;font-size:16.5px;line-height:24px}
.services{left:0;width:575px;top:246px;font-weight:700;font-size:21px;line-height:29px;list-style:none}
.sell{left:0;width:575px;top:450px;font-weight:700}
.sell__ask{font-size:20px;line-height:26px}
.sell__call{font-size:44px;line-height:46px}
.sell__phone{font-size:54px;line-height:54px;color:var(--silver);letter-spacing:1px}
.sell__note{font-size:17px;line-height:20px}
.sectors{left:0;width:575px;top:770px;font-weight:700;font-size:17px}
</style>
</head>
<body>
<section class="card card--front">
  <div class="photo photo--key" role="img" aria-label="Photo of a hand dropping a house key with a house-shaped keyring into an open palm, bright window behind"></div>
  <svg class="swoosh" viewBox="0 0 576 864" aria-hidden="true">
    <path d="M0,532 C120,610 220,690 330,680 C430,670 500,620 576,575 L576,864 L0,864 Z" fill="var(--slate)"/>
    <path d="M0,532 C120,610 220,690 330,680 C430,670 500,620 576,575" fill="none" stroke="var(--rule)" stroke-width="3"/>
  </svg>
  <p class="centered brand brand--front">Bright Path Realty</p>
  <h1 class="centered slogan">Helping Motivated People<br>Achieve Their Real Estate Goals</h1>
  <p class="centered intro">First Time Home Buyer’s Specialists<br>Assisting You with All of Your<br>Real Estate Needs from<br>CREDIT to CLOSING<br>and beyond</p>
  <p class="centered invite">Come to One of Our<br>Monthly First Time Buyer Informational Sessions,<br>Have Your Credit Reviewed and Receive<br>Personalized Home Purchase Plan?</p>
</section>

<section class="card card--back">
  <div class="photo photo--faint" role="img" aria-label="Faint darkened photo of hands exchanging a house key"></div>
  <p class="centered brand brand--back">Bright Path Realty</p>
  <ul class="centered services">
    <li>First Time Buyer Grant Assistance</li>
    <li>Credit Counseling</li>
    <li>Rochester’s Best Realtors</li>
    <li>Customized Property Search</li>
    <li>Closing and Post-Closing Assistance</li>
  </ul>
  <div class="centered sell">
    <p class="sell__ask">Need to Sell Your Property?</p>
    <p class="sell__call">Call us today</p>
    <p class="sell__phone">555-HOME</p>
    <p class="sell__note">for a free consultation</p>
  </div>
  <p class="centered sectors">Residential Investment Commercial</p>
</section>
</body>
</html>
```